The Gilded Otter Espresso Nook Coffee Card

would like a coffee card designed for our café. Most cards are so boring and I need to stand out from the crowd (The Gilded Otter ). I require our logo on one side or the business name also a place for people to write their name and mobile number (collecting data base) and on the back the following
customer gets a stamp for the 1st three coffees purchased, on the 3rd one they get a free upsize. another 2 stamps and on the 3rd one (6) gets a free coffee, another 2 stamps and the customer gets another upsize (9th coffee purchased) and on the 10th card they recivie a voucher for a free pizza.
small print | one free pizza for dinner dining (not available for takeaways and must book), Cant be used with any other offers, opts in to Hear From The Nook if there is a deal on. cant trade for cash or gift

```html
<!DOCTYPE html>
<html lang="en">
<head>
<meta charset="utf-8">
<title>The Gilded Otter Espresso Nook – Coffee Card</title>
<link href="https://fonts.googleapis.com/css2?family=Bebas+Neue&family=Roboto:wght@300&family=Poppins:wght@300;600&display=swap" rel="stylesheet">
<style>
  :root {
    --backdrop: #6e5237;
    --card-white: #ffffff;
    --card-black: #050505;
    --ink: #111111;
    --rule: #333333;
    --silhouette: #2a2a2a;
    --paper-text: #ffffff;
  }
  * { margin: 0; padding: 0; box-sizing: border-box; }
  html, body { width: 900px; height: 1200px; overflow: hidden; }
  body { background: var(--backdrop); position: relative; }

  .card { position: absolute; left: 86px; width: 736px; }

  /* Front */
  .card-front { top: 137px; height: 429px; background: var(--card-white); color: var(--ink); }
  .brand-name {
    position: absolute; left: 30px; right: 36px; top: 60px;
    font-family: "Bebas Neue", sans-serif; font-weight: 400; font-size: 117px; line-height: 1;
    text-align: center; letter-spacing: 1px; white-space: nowrap;
  }
  .rule { position: absolute; left: 40px; right: 46px; height: 2px; background: var(--rule); }
  .rule-top { top: 195px; }
  .rule-mid { top: 269px; }
  .rule-bottom { top: 358px; }
  .brand-tagline {
    position: absolute; left: 40px; right: 46px; top: 213px;
    font-family: "Roboto", sans-serif; font-weight: 300; font-size: 38px; line-height: 1;
    text-align: center; letter-spacing: 1px;
  }
  .holder-row {
    position: absolute; left: 40px; right: 46px; top: 286px; height: 60px;
    display: flex; align-items: center; justify-content: space-between;
    font-family: "Bebas Neue", sans-serif; font-size: 58px; line-height: 1;
  }
  .holder-divider { width: 2px; height: 58px; background: var(--rule); margin-left: 20px; }
  .holder-phone { letter-spacing: 1px; }

  /* Back */
  .card-back { top: 632px; height: 432px; background: var(--card-black); color: var(--paper-text); overflow: hidden; }
  .mascot-area {
    position: absolute; left: 115px; top: 30px; width: 605px; height: 400px;
    background: var(--silhouette); border-radius: 90px 110px 60px 70px;
  }
  .reward-terms {
    position: absolute; left: 40px; right: 40px; top: 67px;
    font-family: "Poppins", sans-serif; font-weight: 600; font-size: 22.5px; line-height: 26.5px;
    text-align: center; white-space: nowrap;
  }
  .back-rule { position: absolute; left: 62px; right: 64px; top: 301px; height: 3px; background: var(--paper-text); }
  .small-print {
    position: absolute; left: 30px; right: 30px; top: 338px;
    font-family: "Poppins", sans-serif; font-weight: 300; font-size: 14.5px; line-height: 21px;
    text-align: center; white-space: nowrap;
  }
</style>
</head>
<body>
  <section class="card card-front">
    <h1 class="brand-name">THE GILDED OTTER</h1>
    <div class="rule rule-top"></div>
    <p class="brand-tagline">ESPRESSO NOOK</p>
    <div class="rule rule-mid"></div>
    <div class="holder-row">
      <span class="holder-name">JORDAN AVERY</span>
      <span class="holder-divider"></span>
      <span class="holder-phone">000 111 222</span>
    </div>
    <div class="rule rule-bottom"></div>
  </section>

  <section class="card card-back">
    <div class="mascot-area" role="img" aria-label="Faint silhouette of the café mascot animal"></div>
    <p class="reward-terms">Customer Gets A Stamp For The 1st Three<br>Coffees Purchased, On The 3rd One They Get A<br>Free Upsize. Another 2 Stamps And On The 3rd<br>One (6) Gets A Free Coffee, Another 2 Stamps<br>And The Customer Gets Another Upsize (9th<br>Coffee Purchased) And On The 10th Card They<br>Recivie A Voucher For A Free Pizza.</p>
    <div class="back-rule"></div>
    <p class="small-print">One Free Pizza For Dinner Dining (Not Available For Takeaways And Must<br>Book), Cant Be Used With Any Other Offers, Opts In To Hear From The Nook<br>If There Is A Deal On. Cant Trade For Cash Or Gift</p>
  </section>
</body>
</html>
```